Luxury Business Card Design for High-End Window Treatments

Gilded Vantages
Custom Plantation Shutters & Architectural Shading Systems

⸻

BACK

Daniel Forsythe
Owner

Custom Interior & Exterior Window Treatments

919-482-7034
gildedvantages.com

I have included a picture that I’m hoping we can use on the back, but I’m also wondering if you can get rid of the ladder? Should we get rid of shutters , shades and blinds underneath Gilded Vantages?

Target Market(s)

High-end residential homeowners, custom home builders, architects, interior designers, and luxury renovation clients seeking premium plantation shutters and motorized architectural shading systems.

Industry/Entity Type

Custom Window treatments

Contact Information for Business Card

Front Gilded Vantages Custom Plantation Shutters Motorized Architectural Shading Systems BACK Daniel Forsythe Owner 919-482-7034 GildedVantages.com Custom Interior & Exterior Window Treatments By Appointment

Requirements
Nice to have
• Not 100% sure on nice to halves or the color but you can definitely check out my website to get a better understanding of what I’m trying to do

```html
<!DOCTYPE html>
<html lang="en">
<head>
<meta charset="utf-8">
<title>Gilded Vantages — Business Card Back</title>
<link rel="stylesheet" href="https://fonts.googleapis.com/css2?family=Marcellus&display=swap">
<style>
  :root {
    --gold: #fcc85a;
    --panel: rgba(40, 42, 50, 0.78);
    --sky: #6fa6dc;
    --house: #8a8478;
    --lawn: #5d6b3a;
  }
  html, body {
    margin: 0;
    padding: 0;
    width: 1200px;
    height: 686px;
    overflow: hidden;
    background: #ffffff;
  }
  .card {
    position: relative;
    width: 1200px;
    height: 686px;
    overflow: hidden;
    font-family: "Marcellus", serif;
  }
  .card__photo {
    position: absolute;
    inset: 0;
    background:
      linear-gradient(180deg,
        var(--sky) 0%,
        #9fb8c4 12%,
        #d9cfb8 18%,
        #3c3f48 26%,
        #3a3d46 45%,
        var(--house) 52%,
        #6b645a 68%,
        var(--lawn) 82%,
        #8b8a7e 100%);
  }
  .card__panel {
    position: absolute;
    left: 197px;
    top: 157px;
    width: 806px;
    height: 370px;
    box-sizing: border-box;
    border: 4px solid var(--gold);
    background: var(--panel);
    color: var(--gold);
    text-align: center;
  }
  .card__name {
    position: absolute;
    left: 0; right: 0;
    top: 22px;
    margin: 0;
    font-size: 54px;
    font-weight: 400;
    letter-spacing: 1px;
    line-height: 1;
  }
  .card__title {
    position: absolute;
    left: 0; right: 0;
    top: 78px;
    margin: 0;
    font-size: 44px;
    line-height: 1;
    letter-spacing: 1px;
  }
  .card__rule {
    position: absolute;
    left: 313px;
    top: 126px;
    width: 178px;
    height: 2px;
    background: var(--gold);
  }
  .card__detail {
    position: absolute;
    left: 0; right: 0;
    margin: 0;
    line-height: 1;
    letter-spacing: 2px;
  }
  .card__phone { top: 160px; font-size: 28px; }
  .card__web { top: 205px; font-size: 28px; }
  .card__service { top: 250px; font-size: 28px; letter-spacing: 2.5px; }
  .card__hours { top: 315px; font-size: 26px; letter-spacing: 2px; text-transform: uppercase; }
</style>
</head>
<body>
  <main class="card">
    <div class="card__photo" role="img" aria-label="Photograph of a two-story home with screened upper porch, white columns, stone chimney wall, landscaped garden and Adirondack chairs on the lawn"></div>
    <section class="card__panel">
      <h1 class="card__name">Daniel Forsythe</h1>
      <p class="card__title">Owner</p>
      <div class="card__rule"></div>
      <p class="card__detail card__phone">919-482-7034</p>
      <p class="card__detail card__web">gildedvantages.com</p>
      <p class="card__detail card__service">Custom Interior &amp; Exterior Window Treatments</p>
      <p class="card__detail card__hours">By Appointment</p>
    </section>
  </main>
</body>
</html>
```